Wedding Invite for Same Sex Marriage

Looking for creative ideas for our wedding invite, then other cards/information to accompany the invite i.e RSVP, Info Card, Wishing Well.We're a same sex male couple. Our thoughts are something along the lines of the Tumbleweed cartoon series. We put something together quickly for our Save The Date attached. These were printed in various bright colours. Don't stick to this design, be creative with the theme.Love to see what ideas you have.

Font styles to use
Sans Serif
Decorative
Script

Colors

Designer to choose colors to be used in the design.

Requirements
Must have
• Standard details of our names, location and time
Nice to have
• Unsure, looking for ideas from a creative crowd. Probably standard print sizes
Should not have
• Traditional, not cutesy cartoon

```html
<!DOCTYPE html>
<html lang="en">
<head>
<meta charset="utf-8">
<title>Archer + Tumbleweed — Wedding Invitation</title>
<link rel="stylesheet" href="https://fonts.googleapis.com/css2?family=Dancing+Script:wght@700&family=Montserrat:wght@300;400&display=swap">
<style>
  :root {
    --paper: #f1f1f0;
    --ink: #111111;
    --place-blue: #4a7a9e;
    --wash-red: #e8456a;
    --wash-pink: #d78ad0;
    --wash-orange: #ee7b2e;
    --wash-yellow: #d9ea7a;
    --wash-green: #3fd855;
    --wash-teal: #3fd6c9;
    --wash-blue: #54aee3;
  }
  * { margin: 0; padding: 0; box-sizing: border-box; }
  html, body { width: 846px; height: 1200px; overflow: hidden; background: var(--paper); }
  .invitation {
    position: relative;
    width: 846px;
    height: 1200px;
    background: var(--paper);
    color: var(--ink);
    font-family: "Montserrat", sans-serif;
  }
  .watercolour-wash {
    position: absolute;
    left: 0;
    top: 60px;
    width: 846px;
    height: 680px;
  }
  .script {
    position: absolute;
    font-family: "Dancing Script", cursive;
    font-weight: 700;
    line-height: 1;
    white-space: nowrap;
  }
  .first-name-one { left: 86px; top: 218px; font-size: 142px; }
  .surname-one { left: 310px; top: 344px; font-size: 42px; }
  .plus-sign {
    position: absolute;
    left: 496px;
    top: 314px;
    width: 42px;
    height: 44px;
  }
  .first-name-two { right: 86px; top: 402px; font-size: 118px; }
  .surname-two { right: 104px; top: 532px; font-size: 44px; }
  .details { position: absolute; left: 0; width: 846px; text-align: center; }
  .invite-line {
    top: 780px;
    font-size: 19px;
    font-weight: 300;
    letter-spacing: 2px;
    line-height: 33px;
  }
  .wedding-date { top: 850px; font-family: "Dancing Script", cursive; font-weight: 700; font-size: 62px; line-height: 1; }
  .time-line { top: 974px; font-size: 19px; font-weight: 300; letter-spacing: 2px; }
  .venue-line { top: 1004px; font-size: 26px; font-weight: 300; letter-spacing: 2px; color: var(--place-blue); }
  .closing-line { top: 1122px; font-size: 17px; font-weight: 300; letter-spacing: 2px; }
</style>
</head>
<body>
<main class="invitation">
  <svg class="watercolour-wash" viewBox="0 0 846 680" role="img" aria-label="Rainbow watercolour paint splash spanning the card behind the couple's names">
    <defs>
      <linearGradient id="washUpper" x1="0" y1="0" x2="1" y2="0">
        <stop offset="0" stop-color="var(--wash-red)"/>
        <stop offset="0.25" stop-color="var(--wash-pink)"/>
        <stop offset="0.48" stop-color="var(--wash-blue)"/>
        <stop offset="0.8" stop-color="var(--wash-blue)"/>
        <stop offset="1" stop-color="var(--wash-teal)"/>
      </linearGradient>
      <linearGradient id="washLower" x1="0" y1="0" x2="1" y2="0">
        <stop offset="0" stop-color="var(--wash-orange)"/>
        <stop offset="0.28" stop-color="var(--wash-orange)"/>
        <stop offset="0.38" stop-color="var(--wash-yellow)"/>
        <stop offset="0.55" stop-color="var(--wash-green)"/>
        <stop offset="1" stop-color="var(--wash-teal)"/>
      </linearGradient>
      <linearGradient id="lowerFade" x1="0" y1="0" x2="0" y2="1">
        <stop offset="0.3" stop-color="#fff" stop-opacity="0"/>
        <stop offset="0.6" stop-color="#fff" stop-opacity="1"/>
      </linearGradient>
      <mask id="lowerMask">
        <rect width="846" height="680" fill="url(#lowerFade)"/>
      </mask>
      <path id="washShape" d="M0 170 L50 160 L100 150 L160 140 L220 110 L280 90 L330 70 L380 60 L420 70 L460 40 L500 80 L520 120 L560 110 L600 140 L640 130 L700 150 L760 120 L800 110 L846 100 L846 600 L800 580 L760 600 L700 590 L640 570 L580 580 L520 610 L470 650 L420 640 L360 600 L320 620 L280 630 L240 620 L200 640 L160 620 L110 630 L60 650 L20 660 L0 640 Z"/>
    </defs>
    <use href="#washShape" fill="url(#washUpper)" opacity="0.8"/>
    <use href="#washShape" fill="url(#washLower)" opacity="0.85" mask="url(#lowerMask)"/>
  </svg>

  <div class="script first-name-one">Archer</div>
  <div class="script surname-one">Hale</div>
  <svg class="plus-sign" viewBox="0 0 42 44" aria-hidden="true">
    <rect x="17" y="0" width="8" height="44" fill="var(--ink)"/>
    <rect x="0" y="18" width="42" height="8" fill="var(--ink)"/>
  </svg>
  <div class="script first-name-two">Tumbleweed</div>
  <div class="script surname-two">Brooks</div>

  <p class="details invite-line">INVITE YOU TO JOIN THEM IN THE CELEBRATION<br>OF THEIR MARRIAGE</p>
  <p class="details wedding-date">Saturday, march 21, 2020</p>
  <p class="details time-line">AT FUN O’CLOCK IN THE EVENING</p>
  <p class="details venue-line">HARMONY HALL, KINDNESS AVENUE, BRISTOL</p>
  <p class="details closing-line">-&nbsp;&nbsp;DINNER AND RECEPTION TO FOLLOW&nbsp;&nbsp;-</p>
</main>
</body>
</html>
```